Photography (and Videography) Flyer required

Am looking for an elegant and very professional looking flyer to promote Corwin Bellamy Photography which services for portrait, fashion, wedding and event photography - aswell as filmmaking, videography services for events such as weddings, conferences etc. The flyer is to be distributed in the New Year and as a promotional offer would like to have a tear off voucher included offering a 50% discount on all bookings. Would also like to include web address which is www.corwinbellamyphotography.example and email address which is enquiry@corwinbellamyphotography.example

(the website will be completed before the flyers are issued)

Target Market(s)

Young adults looking to get married soon and requiring professional photographer/videographer for wedding and related events Adult Males and Females in UK wanted personal fashion photographs of themselves in professional studio environment Parents of young children wanted professional portraits of their children Fashion designers, models, make up artisits looking for professional photographer/filmmaker

Industry/Entity Type

Fashion

Requirements
Must have
• Must be double sided A5 and include a tear off 50% off voucher. Include attractive looking people contained within
Nice to have
• Nice to have logo included
Should not have
• N/A

```html
<!DOCTYPE html>
<html lang="en">
<head>
<meta charset="utf-8">
<title>Corwin Bellamy Photography – Promotional Flyer</title>
<link rel="stylesheet" href="https://fonts.googleapis.com/css2?family=Arimo:wght@400;700&display=swap">
<style>
  :root {
    --stage: #e6e2dc;
    --ink: #050505;
    --purple: #6e1c72;
    --purple-light: #9a4a9d;
    --purple-dark: #4e0f53;
    --voucher: #5c1361;
    --pink: #c64fcd;
    --white: #ffffff;
    --rule: #8b2f90;
  }
  * { box-sizing: border-box; margin: 0; padding: 0; }
  html, body { width: 1200px; height: 900px; overflow: hidden; }
  body {
    background: var(--stage);
    font-family: "Arimo", Arial, sans-serif;
    color: var(--white);
    position: relative;
  }
  .flyer {
    position: absolute;
    top: 55px;
    width: 560px;
    height: 790px;
    background: var(--ink);
    overflow: hidden;
    box-shadow: 0 4px 14px rgba(0,0,0,.25);
  }
  .flyer--front { left: 30px; }
  .flyer--back { left: 610px; }

  .header {
    position: absolute; left: 0; top: 0; width: 100%;
    background: radial-gradient(ellipse at 30% 40%, var(--purple-light) 0%, var(--purple) 45%, var(--purple-dark) 100%);
  }
  .flyer--front .header { height: 150px; }
  .flyer--back .header { height: 215px; }

  .brand {
    position: absolute;
    font-weight: 400;
    color: var(--white);
    line-height: 1.1;
    text-align: center;
  }
  .brand__name { font-size: 30px; letter-spacing: .5px; display: block; }
  .brand__sub { font-size: 14px; letter-spacing: 4px; display: block; margin-top: 4px; }
  .flyer--front .brand { left: 30px; top: 45px; }
  .flyer--back .brand { left: 250px; top: 82px; }

  .camera-icon { position: absolute; left: 320px; top: 36px; }

  .contact-row {
    position: absolute; left: 0; top: 178px; width: 100%;
    display: flex; justify-content: space-between;
    padding: 0 12px 0 16px;
    font-size: 11px; color: var(--pink);
    white-space: nowrap;
  }
  .contact-row__phone { color: var(--white); }

  .voucher { position: absolute; top: 0; }
  .flyer--front .voucher { right: 0; width: 130px; height: 170px; }
  .flyer--back .voucher { left: 0; width: 150px; height: 190px; }
  .voucher svg { display: block; }
  .voucher__text {
    position: absolute;
    width: 100px;
    text-align: center;
    line-height: 1;
    white-space: nowrap;
    transform-origin: center;
  }
  .flyer--front .voucher__text { left: 45px; top: 32px; transform: rotate(52.6deg); }
  .flyer--back .voucher__text { left: -10px; top: 26px; transform: rotate(-51.7deg); }
  .voucher__big { font-size: 22px; font-weight: 700; display: block; }
  .voucher__small { font-size: 12px; display: block; margin-top: 1px; letter-spacing: .3px; }

  .photo { position: absolute; }
  .photo--front {
    left: 290px; top: 235px; width: 270px; height: 555px;
    background: radial-gradient(ellipse at 50% 40%, #d9d9d9 0%, #8c8c8c 40%, #2a2a2a 75%, #050505 100%);
  }
  .photo--back {
    left: 245px; top: 590px; width: 315px; height: 200px;
    background: radial-gradient(ellipse at 40% 55%, #b0607a 0%, #6a2c5c 45%, #2a0e24 80%, #050505 100%);
  }

  .offer { position: absolute; left: 22px; top: 205px; z-index: 2; }
  .offer__percent { font-size: 78px; font-weight: 700; display: inline-block; letter-spacing: -1px; }
  .offer__label { font-size: 24px; display: inline-block; margin-left: 8px; }
  .offer__terms { font-size: 33px; color: var(--pink); margin-top: -4px; }

  .service { position: absolute; left: 6px; z-index: 2; }
  .service--photo { top: 355px; }
  .service--video { top: 535px; }
  .service__title { font-size: 42px; font-weight: 700; line-height: .95; }
  .service__kind { font-size: 38px; line-height: 1; letter-spacing: -.5px; }
  .service__list {
    font-size: 19px; color: var(--pink); text-align: center;
    margin-top: 12px; line-height: 1.3; width: 290px;
  }

  .call-to-action {
    position: absolute; left: 0; top: 705px; width: 280px; z-index: 2;
    font-size: 16px; text-align: center; line-height: 1.3; font-style: italic;
  }

  .about {
    position: absolute; left: 14px; top: 232px; width: 220px;
    font-size: 15px; font-weight: 700; line-height: 1.25;
  }
  .about p { text-align: justify; text-align-last: center; }
  .about p + p { margin-top: 20px; }
  .about__rule {
    width: 110px; height: 2px; margin: 0 auto;
    background: linear-gradient(90deg, transparent, var(--rule), transparent);
  }
  .about__rule--top { margin-bottom: 12px; }
  .about__rule--bottom { margin-top: 18px; }

  .details { position: absolute; left: 255px; top: 330px; }
  .details__item + .details__item { margin-top: 22px; }
  .details__label { font-size: 15px; color: var(--pink); }
  .details__value { font-size: 14px; margin-top: 3px; white-space: nowrap; }
</style>
</head>
<body>

<section class="flyer flyer--front" aria-label="Flyer front">
  <header class="header">
    <div class="brand">
      <span class="brand__name">Corwin Bellamy</span>
      <span class="brand__sub">Photography</span>
    </div>
    <svg class="camera-icon" width="110" height="84" viewBox="0 0 110 84" aria-hidden="true">
      <path d="M8 18 h22 l8 -12 h34 l8 12 h22 a6 6 0 0 1 6 6 v52 a6 6 0 0 1 -6 6 h-94 a6 6 0 0 1 -6 -6 v-52 a6 6 0 0 1 6 -6 z" fill="#fff"/>
      <circle cx="58" cy="48" r="22" fill="#6e1c72"/>
      <circle cx="58" cy="48" r="14" fill="#fff"/>
    </svg>
  </header>

  <div class="contact-row">
    <span class="contact-row__phone">07700 900 418</span>
    <span>www.corwinbellamyphotography.example</span>
    <span>enquiry@corwinbellamyphotography.example</span>
  </div>

  <div class="voucher" aria-label="Tear-off voucher">
    <svg width="130" height="170" viewBox="0 0 130 170" aria-hidden="true">
      <polygon points="0,0 130,0 130,170" fill="var(--voucher)"/>
      <line x1="0" y1="0" x2="130" y2="170" stroke="#000" stroke-width="3" stroke-dasharray="10 6"/>
    </svg>
    <div class="voucher__text">
      <span class="voucher__big">50%</span>
      <span class="voucher__small">DISCOUNT</span>
      <span class="voucher__small">on all bookings</span>
    </div>
  </div>

  <div class="photo photo--front" role="img" aria-label="Black and white studio portrait of a model in a trench coat"></div>

  <div class="offer">
    <span class="offer__percent">50%</span><span class="offer__label">DISCOUNT</span>
    <div class="offer__terms">ON ALL BOOKINGS</div>
  </div>

  <div class="service service--photo">
    <div class="service__title">PROMOTION</div>
    <div class="service__kind">PHOTOGRAPHY</div>
    <div class="service__list">PORTRAIT, FASHION,<br>WEDDING, EVENT COVERAGE</div>
  </div>

  <div class="service service--video">
    <div class="service__title">PROMOTION</div>
    <div class="service__kind">VIDEOGRAPHY</div>
    <div class="service__list">FILM-MAKING, CONFERENCE,<br>WEDDING, EVENT COVERAGE</div>
  </div>

  <p class="call-to-action">Call now for an informal disussion and quotation. Mention this flyer and instantly receive 50% off!</p>
</section>

<section class="flyer flyer--back" aria-label="Flyer back">
  <header class="header">
    <div class="brand">
      <span class="brand__name">Corwin Bellamy</span>
      <span class="brand__sub">Photography</span>
    </div>
  </header>

  <div class="voucher" aria-label="Tear-off voucher">
    <svg width="150" height="190" viewBox="0 0 150 190" aria-hidden="true">
      <polygon points="0,0 150,0 0,190" fill="var(--voucher)"/>
      <line x1="150" y1="0" x2="0" y2="190" stroke="#000" stroke-width="3" stroke-dasharray="10 6"/>
    </svg>
    <div class="voucher__text">
      <span class="voucher__big">50%</span>
      <span class="voucher__small">DISCOUNT</span>
      <span class="voucher__small">on all bookings</span>
    </div>
  </div>

  <div class="about">
    <div class="about__rule about__rule--top"></div>
    <p>Portrait, Fashion and Wedding Photographer. Based in the Heart of the Midlands, with private studio located minutes from Birmingham City Centre. Specialising in creative, contemporary photographic and film production services throughout the UK</p>
    <p>The images captured are full of style, creativity and artistic flair giving you a spectacular collection of photographs, videos to remember your special occasions by.</p>
    <div class="about__rule about__rule--bottom"></div>
  </div>

  <div class="details">
    <div class="details__item">
      <div class="details__label">WEBSITE:</div>
      <div class="details__value">www.corwinbellamyphotography.example</div>
    </div>
    <div class="details__item">
      <div class="details__label">EMAIL:</div>
      <div class="details__value">enquiry@corwinbellamyphotography.example</div>
    </div>
    <div class="details__item">
      <div class="details__label">PHONE:</div>
      <div class="details__value">07700 900 418</div>
    </div>
  </div>

  <div class="photo photo--back" role="img" aria-label="Portrait of a woman in a purple evening dress seated on a leather sofa"></div>
</section>

</body>
</html>
```